A3 Poster & DL Flyer Design Project

We need a poster and flyer designed to advertise a Wine, Food and Live music event.
Event title is "Sunlit Vine Gathering" and is put on by Morrow Creek Wines. Date for the event is Sunday 21 April 2013
The outdoor event covers wine, gourmet food and live music
Live music genera is Jazz, Blues, Swing
Updates

Reason: Most of the designs did not meet our requirements only 3 out of 21 have potential but would like to see more

Target Market(s)

25 - 55 wine drinkers with money.

Industry/Entity Type

Event

Requirements
Must have
• Title of the Event "Sunlit Vine Gathering"
Date Sunday 21 April 2013 or be generic where we can write the date on each year.
Camel Logo
Entry is Free
No BYO Alcohol
Must reflect Wine, Food & Live Music

```html
<!DOCTYPE html>
<html lang="en">
<head>
<meta charset="utf-8">
<title>Sunlit Vine Gathering – Flyer</title>
<link href="https://fonts.googleapis.com/css2?family=Arimo:wght@400;700&family=Cinzel:wght@400&family=Tinos&display=swap" rel="stylesheet">
<style>
  :root {
    --backdrop: #e4e4e4;
    --paper: #f3f3f2;
    --teal: #5f97a8;
    --teal-light: #8fb8c5;
    --navy: #3c5870;
    --red: #e8202a;
    --ink: #2b2b2b;
    --subtitle: #5b97ab;
    --scallop: #8a4a2f;
    --disc: #f1eeec;
    --wood: #a8764b;
    --wood-dark: #7b5433;
    --rope: #c9a66b;
    --wine-dark: #1d1418;
    --wine-mid: #4a3238;
    --glass-light: #d9dcdf;
  }
  * { box-sizing: border-box; margin: 0; padding: 0; }
  html, body { width: 1200px; height: 800px; overflow: hidden; background: var(--backdrop); }
  .canvas { position: relative; width: 1200px; height: 800px; }

  .flyer {
    position: absolute; left: 410px; top: 14px;
    width: 380px; height: 772px;
    background: var(--paper); overflow: hidden;
    font-family: "Arimo", Arial, sans-serif; color: var(--ink);
  }

  .header-band { position: absolute; left: 0; top: 0; width: 100%; height: 140px; }
  .brand-name {
    position: absolute; right: 26px; top: 40px;
    font-family: "Cinzel", Georgia, serif; font-size: 12px; letter-spacing: 1.5px;
    color: var(--ink);
  }

  .entry-seal { position: absolute; right: 8px; top: 76px; width: 104px; height: 104px; }
  .entry-seal svg { position: absolute; inset: 0; width: 100%; height: 100%; }
  .entry-seal__text {
    position: absolute; inset: 0; display: flex; flex-direction: column;
    align-items: center; justify-content: center;
    font-family: "Tinos", "Times New Roman", serif; font-size: 15px; line-height: 1.2;
    color: #fff; letter-spacing: 1px; text-align: center;
  }

  .event-title {
    position: absolute; left: 22px; top: 150px;
    font-weight: 400; font-size: 38px; line-height: 1.03; letter-spacing: -0.5px;
  }
  .event-title .accent { color: var(--red); }
  .event-host {
    position: absolute; left: 22px; top: 236px;
    font-size: 21px; color: var(--subtitle);
  }

  .bottle-photo {
    position: absolute; left: 0; top: 290px; width: 250px; height: 440px;
    background:
      radial-gradient(ellipse at 75% 30%, var(--glass-light) 0%, transparent 45%),
      linear-gradient(180deg, #b9a58c 0%, #8a6d4a 22%, var(--wine-mid) 40%, var(--wine-dark) 100%);
    border-radius: 60px 90px 0 0;
  }

  .highlights { position: absolute; left: 172px; top: 340px; width: 200px; height: 200px; }
  .highlights svg { position: absolute; left: -10px; top: -10px; width: 220px; height: 220px; }
  .highlights__list {
    position: absolute; inset: 0; display: flex; flex-direction: column;
    align-items: center; justify-content: center; list-style: none; gap: 6px;
  }
  .highlights__item { font-size: 20px; }
  .highlights__item--lead { font-size: 28px; }

  .byo-note {
    position: absolute; right: 14px; top: 292px;
    font-family: "Tinos", "Times New Roman", serif; font-size: 15px; line-height: 1.05;
    text-align: right;
  }
  .byo-arrow { position: absolute; left: 262px; top: 326px; width: 100px; height: 60px; }
  .music-arrow { position: absolute; left: 150px; top: 488px; width: 50px; height: 80px; }

  .genre-signs { position: absolute; left: 176px; top: 572px; width: 184px; }
  .genre-sign {
    position: relative; height: 32px; margin-bottom: 10px;
    background: linear-gradient(180deg, var(--wood) 0%, var(--wood-dark) 100%);
    border-radius: 4px; color: #fff; font-size: 19px;
    display: flex; align-items: center; justify-content: center;
  }
  .genre-sign--title { font-weight: 700; font-size: 21px; }
  .genre-sign::before, .genre-sign::after {
    content: ""; position: absolute; top: -12px; width: 2px; height: 12px; background: var(--rope);
  }
  .genre-sign::before { left: 30px; }
  .genre-sign::after { right: 30px; }

  .footer-band { position: absolute; left: 0; bottom: 0; width: 100%; height: 70px; }
</style>
</head>
<body>
<div class="canvas">
  <article class="flyer">
    <svg class="header-band" viewBox="0 0 380 140" preserveAspectRatio="none" aria-hidden="true">
      <path d="M0 0H380V140C300 120 200 90 0 80Z" fill="var(--teal)"/>
      <path d="M0 80C120 86 230 110 380 140V146C230 118 120 96 0 92Z" fill="#fff"/>
      <path d="M0 92C120 98 230 122 380 150V156C230 130 120 108 0 100Z" fill="var(--teal-light)"/>
      <g stroke="#fff" stroke-width="1" opacity=".7" fill="none">
        <path d="M300 0C305 30 300 60 296 90"/>
        <path d="M320 0C322 35 318 70 316 100"/>
        <path d="M340 0C345 30 342 70 336 108"/>
        <path d="M360 0C358 40 362 80 358 118"/>
      </g>
    </svg>
    <div class="brand-name">MORROW CREEK WINES</div>

    <div class="entry-seal">
      <svg viewBox="0 0 120 120" aria-hidden="true">
        <g fill="var(--navy)">
          <rect x="18" y="18" width="84" height="84" transform="rotate(0 60 60)"/>
          <rect x="18" y="18" width="84" height="84" transform="rotate(15 60 60)"/>
          <rect x="18" y="18" width="84" height="84" transform="rotate(30 60 60)"/>
          <rect x="18" y="18" width="84" height="84" transform="rotate(45 60 60)"/>
          <rect x="18" y="18" width="84" height="84" transform="rotate(60 60 60)"/>
          <rect x="18" y="18" width="84" height="84" transform="rotate(75 60 60)"/>
        </g>
        <circle cx="60" cy="60" r="47" fill="none" stroke="#fff" stroke-width="1" stroke-dasharray="2 2"/>
      </svg>
      <div class="entry-seal__text"><span>ENTRY</span><span>IS</span><span>FREE</span></div>
    </div>

    <h1 class="event-title"><span class="accent">Sunlit</span><br><span class="accent">Vine</span> Gathering</h1>
    <p class="event-host">by Morrow Creek Wines</p>

    <div class="bottle-photo" role="img" aria-label="Photo of two red wine bottle necks with foil caps"></div>

    <p class="byo-note">No<br>BYO Alcohol</p>
    <svg class="byo-arrow" viewBox="0 0 100 60" aria-hidden="true">
      <path d="M4 56C40 52 70 36 84 6" fill="none" stroke="var(--ink)" stroke-width="1.5"/>
      <path d="M78 10L85 2L88 13" fill="none" stroke="var(--ink)" stroke-width="1.5"/>
    </svg>

    <div class="highlights">
      <svg viewBox="-10 -10 220 220" aria-hidden="true">
        <g fill="var(--scallop)">
          <circle cx="100" cy="100" r="92"/>
          <circle cx="192" cy="100" r="14"/><circle cx="185" cy="135.2" r="14"/>
          <circle cx="165.1" cy="165.1" r="14"/><circle cx="135.2" cy="185" r="14"/>
          <circle cx="100" cy="192" r="14"/><circle cx="64.8" cy="185" r="14"/>
          <circle cx="34.9" cy="165.1" r="14"/><circle cx="15" cy="135.2" r="14"/>
          <circle cx="8" cy="100" r="14"/><circle cx="15" cy="64.8" r="14"/>
          <circle cx="34.9" cy="34.9" r="14"/><circle cx="64.8" cy="15" r="14"/>
          <circle cx="100" cy="8" r="14"/><circle cx="135.2" cy="15" r="14"/>
          <circle cx="165.1" cy="34.9" r="14"/><circle cx="185" cy="64.8" r="14"/>
        </g>
        <circle cx="100" cy="100" r="90" fill="var(--disc)"/>
        <circle cx="100" cy="100" r="82" fill="none" stroke="var(--scallop)" stroke-width="1" stroke-dasharray="1.5 3"/>
      </svg>
      <ul class="highlights__list">
        <li class="highlights__item highlights__item--lead">Wine</li>
        <li class="highlights__item">Gourmet Food</li>
        <li class="highlights__item">Live Music</li>
      </ul>
    </div>

    <svg class="music-arrow" viewBox="0 0 50 80" aria-hidden="true">
      <path d="M44 6C18 8 8 30 14 70" fill="none" stroke="var(--ink)" stroke-width="1.5"/>
      <path d="M8 62L14 72L20 62" fill="none" stroke="var(--ink)" stroke-width="1.5"/>
    </svg>

    <div class="genre-signs">
      <div class="genre-sign genre-sign--title">Genera</div>
      <div class="genre-sign">Jazz</div>
      <div class="genre-sign">Blues</div>
      <div class="genre-sign">Swing</div>
    </div>

    <svg class="footer-band" viewBox="0 0 380 70" preserveAspectRatio="none" aria-hidden="true">
      <path d="M0 20C60 10 100 30 140 70H0Z" fill="var(--teal)"/>
      <path d="M0 14C60 4 104 26 148 70H140C100 30 60 10 0 20Z" fill="#fff"/>
    </svg>
  </article>
</div>
</body>
</html>
```